Business Card Design Project

I would like a business card created for a new company. This is a holding company that acts as my investment company. It holds real estate and service based companies. The name of the company is Sandorecca which is Italian for Evolution. Defined as development or growth.
We currently have no logo. I really like some of the "different" cards out there. Potentially metallic or grey/black. That looks premium/hi-end and unique. I am not sure if your design would be specific to the card stock I end with our just logo/design/font.
Real Estate

```html
<!DOCTYPE html>
<html lang="it">
<head>
<meta charset="utf-8">
<title>Sandorecca – Business Card</title>
<link rel="stylesheet" href="https://fonts.googleapis.com/css2?family=Arimo:wght@400;700&display=swap">
<style>
  :root {
    --card-edge: #1b2629;
    --card-mid: #2c3b40;
    --card-glow: #4a5c62;
    --band-tone: rgba(125, 144, 149, 0.22);
    --band-top: rgba(111, 129, 134, 0.45);
    --brand-silver: #d2d8da;
    --heading-grey: #c6ced1;
    --body-grey: #d3d9db;
  }
  * { margin: 0; padding: 0; box-sizing: border-box; }
  html, body {
    width: 1200px;
    height: 621px;
    overflow: hidden;
    background: var(--card-edge);
  }
  .card {
    position: relative;
    width: 1200px;
    height: 621px;
    overflow: hidden;
    font-family: "Arimo", Arial, sans-serif;
    background:
      radial-gradient(ellipse 55% 60% at 50% 42%, var(--card-glow) 0%, var(--card-mid) 55%, var(--card-edge) 100%);
  }
  .card__top-band {
    position: absolute;
    left: 0;
    top: 0;
    width: 100%;
    height: 66px;
    background: linear-gradient(to bottom, var(--band-top), rgba(111, 129, 134, 0));
  }
  .card__wave-band {
    position: absolute;
    left: 0;
    top: 470px;
    width: 100%;
    height: 120px;
    background: linear-gradient(to bottom,
      rgba(125, 144, 149, 0) 0%,
      var(--band-tone) 45%,
      rgba(125, 144, 149, 0.12) 75%,
      rgba(125, 144, 149, 0) 100%);
  }
  .brand {
    position: absolute;
    left: 76px;
    top: 86px;
    font-size: 86px;
    font-weight: 700;
    letter-spacing: -3px;
    color: var(--brand-silver);
    line-height: 1;
  }
  .message {
    position: absolute;
    left: 0;
    width: 100%;
    padding-right: 20px;
    top: 284px;
    text-align: center;
  }
  .message__title {
    font-size: 40px;
    font-weight: 700;
    color: var(--heading-grey);
    line-height: 50px;
  }
  .message__body {
    font-size: 38px;
    font-weight: 400;
    color: var(--body-grey);
    line-height: 50px;
  }
</style>
</head>
<body>
  <div class="card">
    <div class="card__top-band" role="img" aria-label="Soft light band with a faint sweeping line along the top edge"></div>
    <div class="card__wave-band" role="img" aria-label="Soft translucent swooping waves across the lower part of the card"></div>

    <div class="brand">Sandorecca</div>

    <div class="message">
      <p class="message__title">Lorem ipsum dolor</p>
      <p class="message__body">
        sit amet, consectetur adipiscing elit. Aenean pellentesque<br>
        ligula sed risus pharetra ac porta neque aliquam. Cras<br>
        ornare felis id libero hendrerit fringilla. Donec hendrerit,<br>
        augue vitae pharetra ultrices, risus ligula
      </p>
    </div>
  </div>
</body>
</html>
```